Website for Apartment Rental in Prague

I would like to create designs of my website focused on luxury apartment rentals in Prague, Czech Republic. I created initial mock-ups, They are all attached. I need to design homepage and subpage. The mock-ups were created by combining elements from different websites that I liked but I need you to create a design that is unique and original. The attached files a only a guidance for the structure of the website but not for the design. Try to be creative.

Industry/Entity Type

Apartment

```html
<!DOCTYPE html>
<html lang="en">
<head>
<meta charset="utf-8">
<title>Maison Vltava Apartments Prague</title>
<link href="https://fonts.googleapis.com/css2?family=Raleway:ital,wght@0,400;0,500;0,600;0,700;1,600&family=Open+Sans:ital,wght@0,400;0,600;1,400;1,600&display=swap" rel="stylesheet">
<style>
:root{
  --orange:#f9b233;
  --orange-deep:#e9a11f;
  --dark:#2b2b2b;
  --ink:#222;
  --text:#444;
  --muted:#777;
  --line:#d9d9d9;
  --white:#fff;
}
*{box-sizing:border-box;margin:0;padding:0}
html,body{width:1200px;height:2903px;overflow:hidden;background:var(--white)}
body{position:relative;font-family:"Open Sans",sans-serif;color:var(--text)}
.abs{position:absolute}
.raleway{font-family:"Raleway",sans-serif}

/* header */
.topbar{position:absolute;left:0;top:0;width:1200px;height:100px;border-bottom:2px solid #555}
.topbar .link{position:absolute;font:500 12px "Raleway",sans-serif;color:var(--ink);text-transform:uppercase}
.brand{position:absolute;left:500px;top:16px;width:200px;text-align:center;font-family:"Raleway",sans-serif;color:var(--ink)}
.brand .name{font:600 20px "Raleway",sans-serif;letter-spacing:1px}
.brand .sub{font:600 10px "Raleway",sans-serif;letter-spacing:3px;margin-top:3px}
.brand .city{font:700 13px "Raleway",sans-serif;letter-spacing:2px}
.brand .tag{font:400 8px "Open Sans",sans-serif;color:var(--orange);margin-top:1px}
.contact{position:absolute;font:400 12px "Open Sans",sans-serif;color:var(--ink);display:flex;align-items:center;gap:8px}
.nav{position:absolute;left:0;top:100px;width:1200px;height:55px;display:flex;justify-content:center;gap:0}
.nav a{font:500 12px "Raleway",sans-serif;color:var(--ink);text-decoration:none;text-transform:uppercase;line-height:55px;padding:0 21px}

/* hero */
.hero{position:absolute;left:0;top:155px;width:1200px;height:522px;
  background:linear-gradient(180deg,#d9d6d1 0%,#bdb8b1 45%,#8f8a84 100%)}
.hero-title{position:absolute;left:0;top:415px;width:1200px;text-align:center;font:700 45px "Raleway",sans-serif;color:var(--white);letter-spacing:2px;text-shadow:0 2px 6px rgba(0,0,0,.35)}
.hero-arrow{position:absolute;top:385px}
.price-tab{position:absolute;left:440px;top:620px;width:320px;height:58px;background:var(--orange);border-radius:60px 60px 0 0;text-align:center;color:var(--white)}
.price-tab .small{font:700 10px "Raleway",sans-serif;letter-spacing:1px;margin-top:10px}
.price-tab .big{font:700 19px "Raleway",sans-serif;letter-spacing:1px;margin-top:2px}

/* booking */
.booking{position:absolute;left:0;top:677px;width:1200px;height:97px;background:var(--orange)}
.booking label{position:absolute;top:22px;font:400 12px "Open Sans",sans-serif;color:var(--white)}
.field{position:absolute;top:42px;height:32px;background:var(--white);border:1px solid #ddd;font:400 11px "Open Sans",sans-serif;color:#999;display:flex;align-items:center;padding-left:10px;gap:6px}
.sel-arrow{position:absolute;right:0;top:0;width:16px;height:30px;background:#eee;border-left:1px solid #ddd}
.btn-dark{position:absolute;top:42px;height:32px;background:var(--dark);color:var(--white);font:600 12px "Open Sans",sans-serif;display:flex;align-items:center;justify-content:center}

/* section headings */
.kicker{position:absolute;left:0;width:1200px;text-align:center;font:500 19px "Raleway",sans-serif;color:var(--ink);letter-spacing:1px;text-transform:uppercase}
.heading{position:absolute;left:0;width:1200px;text-align:center;font:500 26px "Raleway",sans-serif;color:var(--ink);letter-spacing:5px;text-transform:uppercase}
.rule{position:absolute;height:1px;background:#888}
.rule-bold{position:absolute;left:292px;width:616px;height:4px;background:var(--ink)}
.lead{position:absolute;left:0;width:1200px;text-align:center;font:italic 600 16px "Open Sans",sans-serif;color:var(--orange)}
.body-center{position:absolute;left:290px;width:620px;text-align:center;font:400 12px/25px "Open Sans",sans-serif;color:var(--ink)}

/* dark band */
.dark-band{position:absolute;left:0;top:1045px;width:1200px;height:305px;background:var(--dark)}
.dark-band .title{position:absolute;left:0;top:118px;width:1200px;text-align:center;font:500 25px "Raleway",sans-serif;color:var(--orange);letter-spacing:5px}
.dark-band .copy{position:absolute;left:268px;top:168px;width:664px;text-align:center;font:400 11.5px/22px "Open Sans",sans-serif;color:#eee}

/* cards */
.card{position:absolute;width:273px}
.card .photo{width:273px;height:173px;position:relative}
.card .badge{position:absolute;left:0;top:72px;width:90px;height:26px;background:var(--orange);opacity:.85;font:600 9px/26px "Open Sans",sans-serif;color:var(--white);text-align:center}
.card .meta{display:flex;gap:30px;margin-top:12px;font:400 11px "Open Sans",sans-serif;color:var(--ink)}
.card .meta span{display:flex;align-items:center;gap:7px}
.card h3{margin-top:17px;font:500 14px/24px "Raleway",sans-serif;color:var(--ink);text-transform:uppercase;height:50px}
.card p{margin-top:12px;font:400 11px/21px "Open Sans",sans-serif;color:var(--ink);height:44px}
.card hr{border:0;border-top:1px solid var(--line);width:233px;margin-top:6px}
.card .actions{display:flex;gap:18px;margin-top:17px}
.btn{height:32px;border:1px solid var(--ink);font:500 11px/30px "Raleway",sans-serif;color:var(--ink);text-transform:uppercase;text-align:center;background:var(--white)}
.btn.details{width:82px}
.btn.book{width:90px}
.btn.active{background:var(--orange);border-color:var(--orange);color:var(--white)}

/* need to know */
.info{position:absolute;left:766px;top:1863px;width:273px;height:370px;border:1px solid #555}
.info h4{font:500 15px "Raleway",sans-serif;color:var(--ink);padding:20px 18px 0;height:56px;border-bottom:1px solid #555;text-transform:uppercase}
.info .item{padding:20px 20px 16px;border-bottom:1px solid #eee}
.info .item:last-child{border-bottom:0}
.info .row{display:flex;align-items:center;gap:16px;font:500 13px "Raleway",sans-serif;color:var(--ink);text-transform:uppercase}
.info .item p{margin-top:10px;font:400 11px/20px "Open Sans",sans-serif;color:var(--ink)}

/* testimonials */
.testi{position:absolute;left:0;top:2314px;width:1200px;height:308px;background:var(--orange)}
.testi .quote{position:absolute;left:290px;top:128px;width:620px;text-align:center;font:italic 400 11.5px/21px "Open Sans",sans-serif;color:#3a2e12}
.testi .qmark{position:absolute;font:italic 700 26px "Open Sans",sans-serif;color:#3a2e12}
.testi .author{position:absolute;left:0;top:210px;width:1200px;text-align:center;font:600 13px "Open Sans",sans-serif;color:#3a2e12}

/* footer */
.fcol{position:absolute;top:2657px}
.fcol h5{font:500 14px "Raleway",sans-serif;color:var(--ink);text-transform:uppercase;margin-bottom:18px}
.fcol li{list-style:none;font:400 11px/25px "Open Sans",sans-serif;color:var(--ink)}
.social{display:flex;gap:14px;margin-bottom:30px}
.social span{width:22px;height:22px;border-radius:50%;background:var(--ink)}
.foot-line{position:absolute;left:161px;top:2854px;width:878px;height:1px;background:var(--line)}
.copyright{position:absolute;left:0;top:2872px;width:1200px;text-align:center;font:400 11px "Open Sans",sans-serif;color:var(--ink)}
.code{position:absolute;left:950px;top:2872px;font:400 12px "Open Sans",sans-serif;color:var(--ink)}
.message{position:absolute;left:1016px;top:2854px;width:184px;height:49px;background:var(--orange);font:600 11px/49px "Open Sans",sans-serif;color:var(--white);text-align:center;text-transform:uppercase}
</style>
</head>
<body>

<header class="topbar">
  <span class="link" style="left:161px;top:33px">Our Hospitality</span>
  <span class="link" style="left:291px;top:33px">EN &#709;</span>
  <div class="brand">
    <div class="name">Maison Vltava</div>
    <div class="sub">APARTMENTS</div>
    <div class="city">PRAGUE</div>
    <div class="tag">luxury apartments</div>
  </div>
  <div class="contact" style="left:725px;top:21px">
    <svg width="12" height="9" viewBox="0 0 12 9"><rect x=".5" y=".5" width="11" height="8" fill="none" stroke="#f9b233"/><path d="M.5 .5 6 5l5.5-4.5" fill="none" stroke="#f9b233"/></svg>
    reservation@vltavastays.com
  </div>
  <div class="contact" style="left:940px;top:21px">
    <svg width="11" height="11" viewBox="0 0 11 11"><path d="M2 0 4 3 3 4.5c.8 1.5 2 2.7 3.5 3.5L8 7l3 2-1 2C5 11 0 6 0 1z" fill="#f9b233"/></svg>
    420 700 118 204
  </div>
  <div class="contact" style="left:917px;top:67px;font:600 12px 'Raleway',sans-serif">
    <svg width="11" height="10" viewBox="0 0 11 10"><path d="M1 0v10M1 1h9L8 3.5 10 6H1" fill="#f9b233" stroke="#f9b233"/></svg>
    DISCOVER PRAGUE
  </div>
</header>

<nav class="nav">
  <a>Apartments</a><a>Location</a><a>Services</a><a>Gallery</a><a>News</a><a>Exclusive Offers&amp; Tours</a><a>For Families</a><a>Contact Us</a>
</nav>

<div class="hero" role="img" aria-label="Bright modern apartment living room with floating staircase, grey sofa and dining area"></div>
<svg class="hero-arrow" style="left:30px" width="40" height="70" viewBox="0 0 40 70"><path d="M32 4 6 35l26 31" fill="none" stroke="#fff" stroke-width="2"/></svg>
<svg class="hero-arrow" style="left:1130px" width="40" height="70" viewBox="0 0 40 70"><path d="M8 4l26 31L8 66" fill="none" stroke="#fff" stroke-width="2"/></svg>
<h1 class="hero-title">BEING HOME IN PRAGUE</h1>
<div class="price-tab"><div class="small">OFFICIAL SITE</div><div class="big">BEST PRICE GUARANTEED</div></div>

<section class="booking">
  <label style="left:161px">Check in</label>
  <label style="left:281px">Check out</label>
  <label style="left:401px">Adults</label>
  <label style="left:460px">Children</label>
  <label style="left:517px">Infants</label>
  <label style="left:573px">Promotional code</label>
  <div class="field" style="left:161px;width:116px"><svg width="10" height="10"><rect x=".5" y="1.5" width="9" height="8" fill="none" stroke="#999"/></svg>dd/mm/yyyy</div>
  <div class="field" style="left:281px;width:116px"><svg width="10" height="10"><rect x=".5" y="1.5" width="9" height="8" fill="none" stroke="#999"/></svg>dd/mm/yyyy</div>
  <div class="field" style="left:401px;width:55px;color:#333">1<span class="sel-arrow"></span></div>
  <div class="field" style="left:460px;width:53px;color:#333">1<span class="sel-arrow"></span></div>
  <div class="field" style="left:517px;width:52px;color:#333">2<span class="sel-arrow"></span></div>
  <div class="field" style="left:573px;width:172px"></div>
  <div class="btn-dark" style="left:750px;width:122px">Check Availability</div>
  <span class="abs" style="left:878px;top:50px;font:400 11px 'Open Sans',sans-serif;color:#fff">or</span>
  <div class="btn-dark" style="left:896px;width:144px;justify-content:flex-start;padding-left:8px">Select Rental Unit<span class="sel-arrow" style="background:#3a3a3a;border-color:#555;height:32px"></span></div>
</section>

<section>
  <div class="rule" style="left:292px;top:828px;width:230px"></div>
  <div class="rule" style="left:678px;top:828px;width:230px"></div>
  <div class="kicker" style="top:816px">A Different</div>
  <h2 class="heading" style="top:845px">Vision of Travelling</h2>
  <p class="lead" style="top:895px">Something spectacular has arrived in the heart of Europe.</p>
  <p class="body-center" style="top:920px">Steps from Old Town, this rental experience is curated with world-class amenities, exemplary style and a level of convenience you have to experience to believe. Experience the different vision of luxury in center of Prague.</p>
  <div class="rule-bold" style="top:996px"></div>
</section>

<section class="dark-band">
  <svg class="abs" style="left:561px;top:32px" width="78" height="78" viewBox="0 0 78 78">
    <circle cx="39" cy="39" r="36" fill="none" stroke="#f9b233" stroke-width="3"/>
    <rect x="29" y="28" width="20" height="14" rx="4" fill="#f9b233"/>
    <rect x="24" y="36" width="30" height="12" rx="4" fill="#f9b233"/>
    <rect x="27" y="48" width="3" height="5" fill="#f9b233"/><rect x="48" y="48" width="3" height="5" fill="#f9b233"/>
  </svg>
  <h2 class="title">INTERIORS DESIGNED BY MAISON VLTAVA</h2>
  <p class="copy">Maison Vltava apartments offers short term and as well as long term options in our studio apartments and our one bedroom apartment homes. Our luxurious apartments and high quality customer service have allowed us to dominate the Prague apartment market with a proven track record. Our years of experience and knowledge have made us a premier apartment rental company as we continue to stress the importance of servicing individuals and corporations who are seeking the finest accommodations.</p>
</section>
<svg class="abs" style="left:570px;top:1349px" width="60" height="26" viewBox="0 0 60 26"><path d="M0 0h60L30 26z" fill="#2b2b2b"/></svg>

<!-- apartment cards -->
<article class="card" style="left:161px;top:1418px">
  <div class="photo" role="img" aria-label="Studio apartment living room with grey sofa and patterned rug" style="background:linear-gradient(135deg,#e6e8ec,#9aa3ad)"><span class="badge">From 150 USD</span></div>
  <div class="meta"><span><svg width="12" height="8"><path d="M0 0v8M0 5h12v3M3 2h8v3" fill="none" stroke="#555"/></svg>1 bedroom</span><span><svg width="9" height="10"><circle cx="4.5" cy="3" r="2.5" fill="#888"/><path d="M0 10a4.5 4 0 0 1 9 0z" fill="#888"/></svg>max 4 people</span></div>
  <h3>Brand New Luxury Living Shinning Contemporary Design</h3>
  <p>Lorem ipsum dolor sit amet, consectetur adipiscing nec a elementum miam vestibulum mi [...]</p>
  <hr>
  <div class="actions"><span class="btn details active">Details</span><span class="btn book">Book Now</span></div>
</article>

<article class="card" style="left:464px;top:1418px">
  <div class="photo" role="img" aria-label="Bright apartment lounge with green sofa and pendant light" style="background:linear-gradient(135deg,#f1ede6,#b9b09f)"><span class="badge">From 150 USD</span></div>
  <div class="meta"><span><svg width="12" height="8"><path d="M0 0v8M0 5h12v3M3 2h8v3" fill="none" stroke="#555"/></svg>1 bedroom</span><span><svg width="9" height="10"><circle cx="4.5" cy="3" r="2.5" fill="#888"/><path d="M0 10a4.5 4 0 0 1 9 0z" fill="#888"/></svg>max 4 people</span></div>
  <h3>Brand New Zen Luxury Living Apartment in the Center of Prague</h3>
  <p>Lorem ipsum dolor sit amet, consectetur adipiscing nec a elementum miam vestibulum mi [...]</p>
  <hr>
  <div class="actions"><span class="btn details">Details</span><span class="btn book">Book Now</span></div>
</article>

<article class="card" style="left:766px;top:1418px">
  <div class="photo" role="img" aria-label="Sunlit apartment with large windows and lime green seating" style="background:linear-gradient(135deg,#dfe7ec,#8fa0a6)"><span class="badge">From 150 USD</span></div>
  <div class="meta"><span><svg width="12" height="8"><path d="M0 0v8M0 5h12v3M3 2h8v3" fill="none" stroke="#555"/></svg>1 bedroom</span><span><svg width="9" height="10"><circle cx="4.5" cy="3" r="2.5" fill="#888"/><path d="M0 10a4.5 4 0 0 1 9 0z" fill="#888"/></svg>max 4 people</span></div>
  <h3>Expedition Prague! Top Loca' Brand New Apartment</h3>
  <p>Lorem ipsum dolor sit amet, consectetur adipiscing nec a elementum miam vestibulum mi [...]</p>
  <hr>
  <div class="actions"><span class="btn details">Details</span><span class="btn book">Book Now</span></div>
</article>

<article class="card" style="left:161px;top:1863px">
  <div class="photo" role="img" aria-label="Penthouse living room with yellow armchair and garden view" style="background:linear-gradient(135deg,#eef0ee,#a9b3a6)"><span class="badge">From 150 USD</span></div>
  <div class="meta"><span><svg width="12" height="8"><path d="M0 0v8M0 5h12v3M3 2h8v3" fill="none" stroke="#555"/></svg>1 bedroom</span><span><svg width="9" height="10"><circle cx="4.5" cy="3" r="2.5" fill="#888"/><path d="M0 10a4.5 4 0 0 1 9 0z" fill="#888"/></svg>max 4 people</span></div>
  <h3>Rand New Sunny Penthouse with a View of Prague</h3>
  <p>Lorem ipsum dolor sit amet, consectetur adipiscing nec a elementum miam vestibulum mi [...]</p>
  <hr>
  <div class="actions"><span class="btn details">Details</span><span class="btn book">Book Now</span></div>
</article>

<article class="card" style="left:464px;top:1863px">
  <div class="photo" role="img" aria-label="Open plan apartment with dark wood floor and ceiling fans" style="background:linear-gradient(135deg,#cfc7bd,#6e6257)"><span class="badge">From 150 USD</span></div>
  <div class="meta"><span><svg width="12" height="8"><path d="M0 0v8M0 5h12v3M3 2h8v3" fill="none" stroke="#555"/></svg>1 bedroom</span><span><svg width="9" height="10"><circle cx="4.5" cy="3" r="2.5" fill="#888"/><path d="M0 10a4.5 4 0 0 1 9 0z" fill="#888"/></svg>max 4 people</span></div>
  <h3>Brand New Modern Apartment Unbeatable Locat Eon</h3>
  <p>Lorem ipsum dolor sit amet, consectetur adipiscing nec a elementum miam vestibulum mi [...]</p>
  <hr>
  <div class="actions"><span class="btn details">Details</span><span class="btn book">Book Now</span></div>
</article>

<aside class="info">
  <h4>Need to Know</h4>
  <div class="item">
    <div class="row"><svg width="26" height="24" viewBox="0 0 26 24"><rect x="2" y="2" width="16" height="22" fill="#333"/><rect x="18" y="10" width="6" height="14" fill="#333"/><g fill="#fff"><rect x="5" y="5" width="3" height="3"/><rect x="11" y="5" width="3" height="3"/><rect x="5" y="11" width="3" height="3"/><rect x="11" y="11" width="3" height="3"/><rect x="8" y="18" width="4" height="6"/></g></svg>Apartments</div>
    <p>Also available to rent all the apartments together for companies or larger groups.</p>
  </div>
  <div class="item">
    <div class="row"><svg width="24" height="24" viewBox="0 0 24 24"><rect x="1" y="3" width="22" height="20" fill="none" stroke="#333" stroke-width="2"/><rect x="1" y="3" width="22" height="6" fill="#333"/><rect x="6" y="0" width="2" height="6" fill="#333"/><rect x="16" y="0" width="2" height="6" fill="#333"/></svg>Check-out</div>
    <p>12 noon; earliest check-in, 3pm —both are flexible, by arrangement.</p>
  </div>
  <div class="item">
    <div class="row"><svg width="24" height="24" viewBox="0 0 24 24"><path d="M1 1h10l12 12-10 10L1 11z" fill="#333"/><circle cx="6" cy="6" r="2" fill="#fff"/></svg>Rates</div>
    <p>prices from 150 USD per night, including tax</p>
  </div>
</aside>

<section class="testi">
  <div class="rule" style="left:292px;top:62px;width:260px;background:#3a2e12"></div>
  <div class="rule" style="left:648px;top:62px;width:260px;background:#3a2e12"></div>
  <div class="kicker" style="top:50px">Client</div>
  <h2 class="heading" style="top:80px">Testimonials</h2>
  <span class="qmark" style="left:270px;top:118px">&#8220;</span>
  <p class="quote">Sed ut perspiciatis unde omnis iste natus error sit voluptatem accusantium doloremque laudantium, totam rem aperiam, ipsa quae ab illo inventore veritatis et quasi architecto beatae vitae dicta sunt explicabo. Nemo enim ipsam voluptatem quia voluptas sit aspernatur aut odit aut fugit, sed quia consequuntur magni dolores eos qui ratione voluptatem.</p>
  <span class="qmark" style="left:873px;top:152px">&#8221;</span>
  <div class="author">Anna Novak</div>
  <div class="rule-bold" style="top:242px;background:#3a2e12"></div>
</section>

<footer>
  <div class="fcol" style="left:161px"><h5>About</h5><ul><li>Home</li><li>Properties</li><li>Agencies</li><li>News</li><li>About Us</li></ul></div>
  <div class="fcol" style="left:296px"><h5>Apartment Rental</h5><ul><li>Sed uerspiciatiem</li><li>Comnisteatusit</li><li>Sed uerspiciatiem</li><li>Comnisteatusit</li><li>Perspiciatis unde</li></ul></div>
  <div class="fcol" style="left:513px"><h5>Who We Are</h5><ul><li>Sed uterspiciatis</li><li>Comnisteatusit</li><li>Perspiciatis unde</li><li>Sed uerspiciatiem</li><li>Comnisteatusit</li></ul></div>
  <div class="fcol" style="left:708px"><h5>Connect</h5>
    <div class="social"><span></span><span></span><span></span><span></span></div>
    <h5>Policies</h5><ul><li>Privacy</li><li>Complaint and Feedback</li></ul></div>
  <div class="fcol" style="left:927px"><h5>Other Links</h5><ul><li>Sed uerspiciatis</li><li>Sed uerspiciatiem</li><li>Perspiciatis unde</li><li>Sed uerspiciatiem</li><li>Comnisteatusit</li></ul></div>
  <div class="foot-line"></div>
  <p class="copyright">© 2017 Maison Vltava. Privacy Policy | Terms of Use | Contact</p>
  <span class="code">C4</span>
  <div class="message">Please leave a message</div>
</footer>

</body>
</html>
```